Business Card Design x 3

We need 3 card designs for 3 different brands of a company. When these 3 cards are put together to form a square (later will be 4), it is visually connected.

One of their card is already designed, but need some modifications. (attachment)
The card size is 52mm x 89mm

FRONT:
1) Orange slice with spot UV water drops (orange background)
2) Tomato with UV water drops (lime green background)
3) Cupcake with UV water drops (brown Pantone 7603c background)

BACK:
1) Orange slice (green background)
2) Tomato (brown background)
3) Cupcake (orange background)
Please put dummy address, tel, fax, email, website first
Solid background
Please allocate a space for Logo placement

Their styles are: Fresh, Friendly, Colorful
***Use Real pictures***

Food & Beverage Industry.

Due to company's information disclosure issue, please private message us or Please send email to studio@velmora-k.com for more information
Updates

The back of the card: Please put a background color with dummy text, we will add in the text later.

Target Market(s)

Adults

Industry/Entity Type

Business

Font styles to use
Sans Serif

Colors
acd036
faa54b

Requirements
Must have
• Each card has different color
Nice to have
• Real Pictures
Should not have
• Graphic elements

```html
<!DOCTYPE html>
<html lang="en">
<head>
<meta charset="utf-8">
<title>Business Card Set – Fresh Series</title>
<link rel="stylesheet" href="https://fonts.googleapis.com/css2?family=Arimo:wght@400;700&display=swap">
<style>
  :root {
    --backdrop: #c8c0b5;
    --orange: #faa54b;
    --lime: #acd036;
    --brown: #654130;
    --ink-brown: #6a4227;
    --ink-lime: #acd036;
  }
  * { margin: 0; padding: 0; box-sizing: border-box; }
  html, body { width: 1200px; height: 1000px; overflow: hidden; }
  body {
    background: var(--backdrop);
    font-family: "Arimo", Arial, sans-serif;
    position: relative;
  }
  .card {
    position: absolute;
    overflow: hidden;
    box-shadow: 0 2px 6px rgba(0,0,0,0.18);
  }
  .card--orange { left: 321px; top: 46px; width: 264px; height: 453px; background: var(--orange); }
  .card--tomato { left: 585px; top: 46px; width: 264px; height: 453px; background: var(--lime); }
  .card--cupcake { left: 321px; top: 499px; width: 260px; height: 445px; background: var(--brown); }

  .card__photo { position: absolute; left: 0; top: 0; width: 100%; height: 100%; }

  .contact {
    position: absolute;
    text-align: center;
    color: var(--ink-brown);
  }
  .card--cupcake .contact { color: var(--ink-lime); }
  .contact__name {
    font-weight: 700;
    font-size: 26px;
    letter-spacing: 0.2px;
    line-height: 1;
    padding-bottom: 2px;
    border-bottom: 1px solid currentColor;
    display: inline-block;
  }
  .contact__role { font-size: 22px; line-height: 1.3; margin-top: 2px; }
  .contact__email {
    font-weight: 700; font-size: 17px; margin-top: 12px;
    display: flex; align-items: center; justify-content: center; gap: 4px;
  }
  .contact__phone {
    font-size: 13px; margin-top: 6px;
    display: flex; align-items: center; justify-content: center; gap: 4px;
  }
  .icon { width: 16px; height: 12px; fill: currentColor; }
  .icon--phone { width: 13px; height: 12px; }

  .card--orange .contact { left: 20px; top: 100px; width: 240px; }
  .card--tomato .contact { left: 20px; top: 91px; width: 238px; }
  .card--cupcake .contact { left: 20px; top: 249px; width: 236px; }
</style>
</head>
<body>

<section class="card card--orange">
  <svg class="card__photo" viewBox="0 0 264 453" role="img" aria-label="Photo of an orange slice with water drops">
    <defs>
      <radialGradient id="orangeSlice" cx="264" cy="453" r="265" gradientUnits="userSpaceOnUse">
        <stop offset="0" stop-color="#f7a21a"/>
        <stop offset="0.85" stop-color="#f39a12"/>
        <stop offset="0.93" stop-color="#ffd23a"/>
        <stop offset="1" stop-color="#fff3b0"/>
      </radialGradient>
    </defs>
    <path d="M264 253 A262 200 0 0 0 2 453 L264 453 Z" fill="url(#orangeSlice)"/>
  </svg>
  <div class="contact">
    <div class="contact__name">MARCUS LEE</div>
    <div class="contact__role">General Manager</div>
    <div class="contact__email">
      <svg class="icon" viewBox="0 0 16 12"><path d="M0 0h16v12H0z M1.5 1.5 8 7l6.5-5.5z" fill-rule="evenodd"/></svg>
      marcus@velmora-k.com
    </div>
    <div class="contact__phone">
      <svg class="icon icon--phone" viewBox="0 0 13 12"><path d="M1 3c0-2 3-2.5 5.5-2.5S12 1 12 3v1H9V2.5H4V4H1z M2.5 5h8l1.5 6H1z"/></svg>
      +65 5210 7781
    </div>
  </div>
</section>

<section class="card card--tomato">
  <svg class="card__photo" viewBox="0 0 264 453" role="img" aria-label="Photo of a tomato slice with water drops">
    <defs>
      <radialGradient id="tomatoSlice" cx="0" cy="453" r="260" gradientUnits="userSpaceOnUse">
        <stop offset="0" stop-color="#e8472a"/>
        <stop offset="0.8" stop-color="#e03a22"/>
        <stop offset="1" stop-color="#d13320"/>
      </radialGradient>
    </defs>
    <path d="M0 256 A258 197 0 0 1 258 453 L0 453 Z" fill="url(#tomatoSlice)"/>
  </svg>
  <div class="contact">
    <div class="contact__name">MARCUS LEE</div>
    <div class="contact__role">General Manager</div>
    <div class="contact__email">
      <svg class="icon" viewBox="0 0 16 12"><path d="M0 0h16v12H0z M1.5 1.5 8 7l6.5-5.5z" fill-rule="evenodd"/></svg>
      marcus@velmora-k.com
    </div>
    <div class="contact__phone">
      <svg class="icon icon--phone" viewBox="0 0 13 12"><path d="M1 3c0-2 3-2.5 5.5-2.5S12 1 12 3v1H9V2.5H4V4H1z M2.5 5h8l1.5 6H1z"/></svg>
      +65 5210 7781
    </div>
  </div>
</section>

<section class="card card--cupcake">
  <svg class="card__photo" viewBox="0 0 260 445" role="img" aria-label="Photo of a frosted cupcake with orange sprinkles and water drops">
    <defs>
      <radialGradient id="cupcakeTop" cx="260" cy="0" r="260" gradientUnits="userSpaceOnUse">
        <stop offset="0" stop-color="#fbf6ec"/>
        <stop offset="0.75" stop-color="#f0e6d4"/>
        <stop offset="0.92" stop-color="#d9c7a8"/>
        <stop offset="1" stop-color="#8a6a48"/>
      </radialGradient>
    </defs>
    <path d="M0 0 L260 0 L260 240 A262 240 0 0 1 0 0 Z" fill="url(#cupcakeTop)"/>
  </svg>
  <div class="contact">
    <div class="contact__name">MARCUS LEE</div>
    <div class="contact__role">General Manager</div>
    <div class="contact__email">
      <svg class="icon" viewBox="0 0 16 12"><path d="M0 0h16v12H0z M1.5 1.5 8 7l6.5-5.5z" fill-rule="evenodd"/></svg>
      marcus@velmora-k.com
    </div>
    <div class="contact__phone">
      <svg class="icon icon--phone" viewBox="0 0 13 12"><path d="M1 3c0-2 3-2.5 5.5-2.5S12 1 12 3v1H9V2.5H4V4H1z M2.5 5h8l1.5 6H1z"/></svg>
      +65 5210 7781
    </div>
  </div>
</section>

</body>
</html>
```